Bright Meadow Counseling Business Card design with a visually interesting use of Space

I need business cards that are luxurious and give a peaceful, calm vibe. I also had some letterhead designed, and i like the look of it also, it's attached with the logo design for reference/ ideas but feel free to be creative.

Target Market(s)

High end luxurious client who needs counseling

Industry/Entity Type

Marriage and Family Therapy

Contact Information for Business Card

Mira Kowalczyk MS LMFT/ or Toby Hallett address 4150 Larkin Suite 600

Font styles to use
Sans Serif

Colors
0054AA
0677BA
7BADD7
CADEEF
E8F1F8
0094D4
00A9DD
6FCCEA
C7EBF8
E9F6FB
A7469A
B969AE
D3A5CF
EDDBEB
F8F0F9
6B429C
8869AF
B7A5CE
E3DAEB
F3F0F8

Requirements
Must have
• Logo and color scheme but be simple modern and luxurious
Nice to have
• I'd like to incorporate some elelmets from the logo and letterhead into a simple modern card

```html
<!DOCTYPE html>
<html lang="en">
<head>
<meta charset="utf-8">
<title>Bright Meadow Counseling – Business Card</title>
<link rel="stylesheet" href="https://fonts.googleapis.com/css2?family=Jost:wght@300&family=Poppins:wght@400;500&display=swap">
<style>
  :root {
    --backdrop: #ececec;
    --card: #ffffff;
    --violet: #8e3fa5;
    --plum: #a7469a;
    --teal: #2fb8b5;
    --lavender: #8869af;
    --ink: #1e1e1e;
    --soft-blue: #e8f1f8;
    --soft-teal: #e9f6fb;
    --soft-pink: #f8f0f9;
  }
  * { margin: 0; padding: 0; box-sizing: border-box; }
  html, body { width: 1200px; height: 1000px; overflow: hidden; }
  body { background: var(--backdrop); position: relative; font-family: "Poppins", sans-serif; }

  .card {
    position: absolute; left: 295px; width: 612px; height: 355px;
    background: var(--card);
    border-radius: 40px 40px 0 40px;
    overflow: hidden;
  }
  .card--front { top: 113px; }
  .card--back { top: 531px; }

  /* front */
  .brand-mark {
    position: absolute; left: 0; right: 0; top: 118px;
    display: flex; align-items: center; justify-content: center; gap: 18px;
  }
  .brand-mark__dot { width: 34px; height: 34px; border-radius: 50%; background: var(--lavender); }
  .brand-mark__name {
    display: flex; flex-direction: column; align-items: flex-end;
    font-family: "Jost", sans-serif; font-weight: 300; color: var(--lavender);
  }
  .brand-mark__line1 { font-size: 44px; line-height: 1.05; }
  .brand-mark__line2 { font-size: 24px; line-height: 1.1; letter-spacing: 2.5px; }

  /* back */
  .brand-small {
    position: absolute; left: 37px; top: 56px;
    display: flex; flex-direction: column; align-items: flex-end;
    font-family: "Jost", sans-serif; font-weight: 300; color: var(--ink);
  }
  .brand-small__line1 { font-size: 22px; line-height: 1.1; }
  .brand-small__line2 { font-size: 12.5px; line-height: 1.2; letter-spacing: 1.2px; }

  .wash {
    position: absolute; left: 185px; top: 114px; width: 427px; height: 241px;
    background:
      radial-gradient(circle at 55% 30%, var(--soft-teal) 0, transparent 45%),
      radial-gradient(circle at 80% 40%, var(--soft-blue) 0, transparent 55%),
      radial-gradient(circle at 30% 80%, #f1f6fa 0, transparent 50%),
      radial-gradient(circle at 100% 95%, var(--soft-pink) 0, transparent 35%);
  }
  .person { position: absolute; left: 25px; top: 145px; }
  .person__name { font-weight: 500; font-size: 20px; color: var(--violet); line-height: 1.2; }
  .person__title { font-size: 13px; color: var(--ink); margin-top: 2px; }

  .rules { position: absolute; left: 27px; top: 296px; height: 3px; width: 561px; }
  .rule { position: absolute; top: 0; height: 3px; }
  .rule--mail { left: 0; width: 267px; background: var(--violet); }
  .rule--phone { left: 273px; width: 104px; background: var(--plum); }
  .rule--place { left: 382px; width: 179px; background: var(--teal); }

  .contact {
    position: absolute; top: 309px; display: flex; align-items: center; gap: 6px;
    font-size: 13.5px; color: var(--ink); white-space: nowrap;
  }
  .contact--mail { left: 27px; }
  .contact--phone { left: 300px; }
  .contact--place { left: 409px; }
  .contact svg { display: block; flex: none; }
</style>
</head>
<body>
  <section class="card card--front">
    <div class="brand-mark">
      <span class="brand-mark__dot"></span>
      <span class="brand-mark__name">
        <span class="brand-mark__line1">Bright Meadow</span>
        <span class="brand-mark__line2">Counseling</span>
      </span>
    </div>
  </section>

  <section class="card card--back">
    <div class="wash" role="img" aria-label="Soft pastel wash of overlapping translucent circles"></div>
    <div class="brand-small">
      <span class="brand-small__line1">Bright Meadow</span>
      <span class="brand-small__line2">Counseling</span>
    </div>

    <div class="person">
      <p class="person__name">Mira Kowalczyk MS LMFT</p>
      <p class="person__title">Behavioral Health Therapist</p>
    </div>

    <div class="rules">
      <span class="rule rule--mail"></span>
      <span class="rule rule--phone"></span>
      <span class="rule rule--place"></span>
    </div>

    <p class="contact contact--mail">
      <svg width="14" height="11" viewBox="0 0 14 11"><rect x="0" y="0" width="14" height="11" rx="1" fill="#8e3fa5"/><path d="M1 1.5 L7 6 L13 1.5" stroke="#fff" stroke-width="1.3" fill="none"/></svg>
      mira@brightmeadowcounsel.com
    </p>
    <p class="contact contact--phone">
      <svg width="11" height="19" viewBox="0 0 11 19"><rect x="0.8" y="0.8" width="9.4" height="17.4" rx="1.8" stroke="#a7469a" stroke-width="1.6" fill="none"/><circle cx="5.5" cy="15.3" r="1" fill="#a7469a"/></svg>
      555.014.2286
    </p>
    <p class="contact contact--place">
      <svg width="12" height="16" viewBox="0 0 12 16"><path d="M6 0 C2.7 0 0 2.6 0 5.9 C0 10 6 16 6 16 C6 16 12 10 12 5.9 C12 2.6 9.3 0 6 0 Z" fill="#2fb8b5"/><circle cx="6" cy="6" r="2.2" fill="#fff"/></svg>
      4150 Larkin Suite 600
    </p>
  </section>
</body>
</html>
```